Brisk Tide needs a web page for E-commerce site

Small startup business looking for a custom website for my New Saltwater apparel Co.

COMPANY OVERVIEW

Brisk Tide was founded In Mont Belvieu, Tx, right on the heart of pelham cove.

Brisk Tide is the adrenaline, sweat pumping moment you find yourself setting the hook on a monster fish. This is the moment when all your senses come to life as you work to land that trophy, and after a grueling fight when your hi-fiving your fishing buddies...It's that moment... when the waters and the air around you are Brisk Sweet....All or Nothing...pure Addiction......This is BRISK TIDE

Looking for a sharp clean sexy web page for my ecommerce page

I like the look of black background websites.

www.brisktide-demo.com
Updates

I am using shopvane as my host site if that means anything to y'all

Thank you all for the submissions! There were some great ones!  I will have more projects in the future. thanks again

Target Market(s)

inshore/offshore fishing, saltwater enthusiast

Industry/Entity Type

Business

Requirements
Must have
• logo's

inshore/offshore fishing appeal

compatible with shopvane site

```html
<!DOCTYPE html>
<html lang="en">
<head>
<meta charset="utf-8">
<title>Brisk Tide</title>
<link rel="stylesheet" href="https://fonts.googleapis.com/css2?family=Arimo:wght@400;700&display=swap">
<style>
  :root {
    --sea-light: #3a9aa4;
    --sea-mid: #1b6573;
    --sea-deep: #0b2838;
    --sea-abyss: #06141f;
    --text-light: #ffffff;
    --button-fill: #f9fa5c;
    --button-ink: #1f2fd6;
    --button-edge: #1f3ae0;
  }
  * { box-sizing: border-box; margin: 0; padding: 0; }
  html, body { width: 1200px; height: 675px; overflow: hidden; }
  body { font-family: "Arimo", Arial, sans-serif; color: var(--text-light); }
  .page { position: relative; width: 1200px; height: 675px; overflow: hidden; }
  .hero-backdrop {
    position: absolute; inset: 0;
    background:
      radial-gradient(ellipse 700px 420px at 260px 120px, var(--sea-light) 0%, transparent 70%),
      linear-gradient(180deg, var(--sea-mid) 0%, var(--sea-deep) 62%, var(--sea-abyss) 100%);
  }
  .brand-mark {
    position: absolute; left: 22px; top: 72px;
    font-weight: 700; font-size: 28px; letter-spacing: 1px;
    display: flex; align-items: center; gap: 8px;
  }
  .brand-mark .dot { width: 10px; height: 10px; border-radius: 50%; background: var(--text-light); }
  .shop-nav { position: absolute; left: 360px; top: 73px; }
  .shop-nav .label { font-weight: 700; font-size: 14px; text-shadow: 0 1px 2px rgba(0,0,0,.4); }
  .colour-buttons { position: absolute; top: 28px; left: 55px; display: flex; gap: 49px; list-style: none; }
  .colour-buttons a {
    display: block; width: 162px; height: 36px; line-height: 32px;
    background: var(--button-fill); border-bottom: 4px solid var(--button-edge);
    color: var(--button-ink); font-weight: 700; font-size: 11px;
    text-align: center; text-decoration: none;
  }
  .hero-title {
    position: absolute; left: 0; right: 0; top: 230px;
    text-align: center; font-weight: 700; font-size: 138px; letter-spacing: 4px;
    line-height: 1;
  }
  .hero-story {
    position: absolute; left: 236px; width: 728px; top: 476px;
    text-align: center; font-size: 12.5px; line-height: 17px;
    text-shadow: 0 1px 2px rgba(0,0,0,.6);
  }
</style>
</head>
<body>
<main class="page">
  <div class="hero-backdrop" role="img" aria-label="Underwater photo of a large school of silver fish swirling in blue-green water"></div>

  <div class="brand-mark"><span>Brisk Tide</span><span class="dot"></span></div>

  <nav class="shop-nav">
    <p class="label">apparel</p>
    <ul class="colour-buttons">
      <li><a href="#">White</a></li>
      <li><a href="#">Black</a></li>
      <li><a href="#">Yellow</a></li>
    </ul>
  </nav>

  <h1 class="hero-title">BRISK TIDE</h1>

  <p class="hero-story">Brisk Tide is the adrenaline, sweat pumping moment you find yourself setting the hook on a monster fish. This is the moment when all your senses come to life as you work to land that trophy, and after a grueling fight when your hi-fiving your fishing buddies...It's that moment... when the waters and the air around you are Brisk Sweet....All or Nothing...pure Addiction......This is BRISK TIDE</p>
</main>
</body>
</html>
```